UK landscaping company needs website

We, Brackwell Landscapes need a website design for a company based in Surrey, UK. The design should be bold and playful. We have three main areas of work driveways, paving and fencing. It shouldn't be too heavy in text and concentrate on the pictures from previous jobs we've completed. You may use stock images for the design, these can be changed if you are successful. Please don’t just copy the flyer it is just there to provide content.
We have a logo design which we would also like editing slightly.
Here are some of my local competitors
https://www.fernivalelandscapes.co.uk/

https://www.twinbirchgardendesign.com/

https://mallowbecklandscapes.co.uk/

Industry/Entity Type

Landscaping

Coding

Coded - Design and coding required

Number of Pages Required

3 page

Font styles to use
Sans Serif

Requirements
Must have
• Pictures of my previous jobs.
Must be mobile friendly
Easy to navigate
Nice to have
• Try to use different colours. It would be good to have some designs that aren’t just black and green.
I’d like some curves in the design.
Should not have
• We install hard landscaping. Think more building/construction and less plants and cutting grass.

```html
<!DOCTYPE html>
<html lang="en">
<head>
<meta charset="utf-8">
<title>Brackwell Landscapes</title>
<link href="https://fonts.googleapis.com/css2?family=Montserrat:wght@400;600;700;800&family=Open+Sans:ital,wght@0,400;0,600;1,400&display=swap" rel="stylesheet">
<style>
:root{
  --green:#6abf2e;
  --green-dark:#4f9a1c;
  --ink:#1d1d1d;
  --body:#555555;
  --paper:#ffffff;
  --mist:#efefef;
  --night:#0b0b0b;
  --muted:#9a9a9a;
}
*{box-sizing:border-box;margin:0;padding:0}
html,body{width:1200px;height:4160px;overflow:hidden;background:var(--paper)}
body{font-family:"Open Sans",Arial,sans-serif;color:var(--body)}
.page{position:relative;width:1200px;height:4160px;overflow:hidden}
.abs{position:absolute}
.heading{font-family:"Montserrat",Arial,sans-serif;font-weight:800;color:var(--ink);text-transform:uppercase;letter-spacing:1px}
.heading .accent{color:var(--green)}
.btn{display:inline-block;font-family:"Montserrat",Arial,sans-serif;font-weight:700;font-size:15px;text-transform:uppercase;letter-spacing:1px;border-radius:30px}

/* hero */
.hero{left:0;top:0;width:1200px;height:900px;background:linear-gradient(180deg,#3a3128 0%,#51463a 30%,#4f6a2d 55%,#5f8a2e 75%,#3d5a22 100%)}
.nav{left:0;top:30px;width:1200px;height:70px}
.nav a{position:absolute;top:40px;color:#fff;font-family:"Montserrat",Arial,sans-serif;font-size:14px;font-weight:600;text-decoration:none;text-transform:uppercase}
.nav a.active{color:var(--green)}
.nav-brand{position:absolute;left:0;width:1200px;top:10px;text-align:center;color:#fff;font-family:"Montserrat",Arial,sans-serif;font-weight:800;font-size:30px;letter-spacing:2px;text-transform:uppercase}
.nav-phone{position:absolute;right:66px;top:-12px;color:var(--green);font-family:"Montserrat",Arial,sans-serif;font-weight:600;font-size:20px;display:flex;align-items:center;gap:8px}
.hero-brand{left:0;top:220px;width:1200px;text-align:center;color:#fff;font-family:"Montserrat",Arial,sans-serif;font-weight:800;font-size:74px;line-height:1.05;letter-spacing:3px;text-transform:uppercase}
.hero-cta{left:492px;top:466px;width:216px;height:52px;line-height:48px;text-align:center;color:#fff;border:2px solid #fff;background:rgba(0,0,0,.35)}

/* welcome */
.welcome-title{left:160px;top:890px;font-size:46px;line-height:58px}
.welcome-copy{left:160px;top:1015px;width:450px;font-size:15px;line-height:22px}
.welcome-btn{left:160px;top:1208px;width:160px;height:46px;line-height:46px;text-align:center;color:#fff;background:var(--green)}

/* services */
.services-bg{left:0;top:1300px;width:1200px;height:960px;background:linear-gradient(180deg,#f4f4f4,#e9e9e9)}
.services-title{left:0;top:1478px;width:1200px;text-align:center;font-size:46px}
.services-intro{left:320px;top:1550px;width:560px;text-align:center;font-size:15px;line-height:22px}
.service{top:1640px;width:300px;text-align:center}
.service-photo{width:250px;height:250px;margin:0 auto;border-radius:50%;border:9px solid var(--green)}
.service-name{margin-top:40px;color:var(--green);font-family:"Montserrat",Arial,sans-serif;font-size:20px;font-weight:600}
.service-text{margin:14px auto 0;width:220px;font-size:14px;line-height:21px}
.arrow{top:1720px}

/* gallery */
.gallery-title{left:0;top:2310px;width:1200px;text-align:center;font-size:46px}
.gallery-intro{left:320px;top:2385px;width:560px;text-align:center;font-size:15px;line-height:22px}
.tile{display:block}

/* testimonials */
.reviews-bg{left:0;top:3040px;width:1200px;height:640px;background:linear-gradient(180deg,#f3f3f3,#e6e6e6)}
.reviews-title{left:0;top:3268px;width:1200px;text-align:center;font-size:44px}
.reviews-quote{left:180px;top:3340px;width:840px;text-align:center;font-size:15px;line-height:22px}
.reviews-name{left:0;top:3478px;width:1200px;text-align:center;color:var(--green);font-family:"Montserrat",Arial,sans-serif;font-size:22px;font-weight:600}
.reviews-dots{left:0;top:3530px;width:1200px;display:flex;justify-content:center;gap:12px}
.reviews-dots span{width:18px;height:18px;border-radius:50%;background:#9d9d9d}
.reviews-dots span.on{background:#5e5e5e}

/* footer */
.footer{left:0;top:3660px;width:1200px;height:500px;background:var(--night)}
.footer-brand{left:170px;top:3862px;color:#fff;font-family:"Montserrat",Arial,sans-serif;font-weight:800;font-size:38px;line-height:44px;text-transform:uppercase;letter-spacing:1px}
.social{left:196px;top:3960px;display:flex;gap:18px}
.social span{width:18px;height:18px;border-radius:50%;background:var(--green)}
.contact{left:455px;width:260px;display:flex;gap:14px;align-items:flex-start;color:#fff;font-size:14px;line-height:20px}
.contact svg{flex:none}
.form{left:775px;top:3800px;width:340px}
.form-label{color:var(--green);font-family:"Montserrat",Arial,sans-serif;font-size:14px;font-weight:600;margin-bottom:14px}
.field{color:#cfcfcf;font-size:13px;padding-bottom:12px;border-bottom:1px solid #555;margin-bottom:24px}
.field.tall{height:82px}
.submit{width:110px;height:38px;line-height:38px;text-align:center;background:var(--green);color:#fff;font-size:13px}
.copyright{left:0;top:4112px;width:1200px;text-align:center;color:#bbb;font-size:12px;letter-spacing:1px;text-transform:uppercase}
</style>
</head>
<body>
<div class="page">

  <!-- hero -->
  <div class="abs hero" role="img" aria-label="Photograph of a finished back garden with new lawn, timber-edged raised bed and paved seating area beside a fence"></div>
  <nav class="abs nav">
    <a class="active" style="left:172px">Home</a>
    <a style="left:240px">About Us</a>
    <a style="left:340px">Our Services</a>
    <div class="nav-brand">Brackwell</div>
    <a style="left:760px">Contracts</a>
    <a style="left:866px">Gallery</a>
    <a style="left:956px">Contact</a>
    <div class="nav-phone">
      <svg width="20" height="20" viewBox="0 0 24 24"><path fill="#6abf2e" d="M6.6 10.8a15 15 0 0 0 6.6 6.6l2.2-2.2c.3-.3.7-.4 1-.2 1.1.4 2.3.6 3.6.6.6 0 1 .4 1 1V20c0 .6-.4 1-1 1A17 17 0 0 1 3 4c0-.6.4-1 1-1h3.5c.6 0 1 .4 1 1 0 1.3.2 2.5.6 3.6.1.3 0 .7-.2 1z"/></svg>
      Call:01632 960 418
    </div>
  </nav>
  <div class="abs hero-brand">Brackwell<br>Landscapes</div>
  <div class="abs btn hero-cta">View Projects</div>

  <svg class="abs" style="left:0;top:620px" width="1200" height="300" viewBox="0 620 1200 300">
    <path d="M0 846 C 380 880, 820 800, 1200 640 L1200 920 L0 920 Z" fill="#ffffff"/>
    <path d="M0 836 C 380 870, 820 790, 1200 630" fill="none" stroke="#6abf2e" stroke-width="6"/>
  </svg>

  <!-- welcome -->
  <h1 class="abs heading welcome-title">Welcome to<br><span class="accent">Brackwell Landscapes</span></h1>
  <p class="abs welcome-copy">From new driveways to patios, walls and fences, we build outdoor spaces made to last. Our team works across Surrey with quality stone, brick and timber, and we take care of every stage, from the first visit and clear quote to the final sweep. Each job is planned around your home, your budget and how you want to use the space. We turn up on time, keep sites tidy and finish the work properly, so you can enjoy it for years.</p>
  <div class="abs btn welcome-btn">Read More</div>

  <!-- services -->
  <div class="abs services-bg"></div>
  <svg class="abs" style="left:0;top:1280px" width="1200" height="160" viewBox="0 1280 1200 160">
    <path d="M0 1280 L1200 1280 L1200 1320 C 860 1430, 360 1440, 0 1330 Z" fill="#ffffff"/>
    <path d="M0 1326 C 360 1436, 860 1426, 1200 1316" fill="none" stroke="#6abf2e" stroke-width="7"/>
  </svg>
  <h2 class="abs heading services-title">Our <span class="accent">Services</span></h2>
  <p class="abs services-intro">Hard landscaping built with care, from the ground up. Driveways, paving and fencing laid by a skilled local team who take pride in every detail.</p>

  <div class="abs service" style="left:140px">
    <div class="service-photo" role="img" aria-label="Photograph of a grey stone paved driveway" style="background:linear-gradient(135deg,#b9b8b4,#8e8d89)"></div>
    <div class="service-name">Work Driveways</div>
    <p class="service-text">Block paving, resin and gravel drives laid on a solid base for years of use.</p>
  </div>
  <div class="abs service" style="left:450px">
    <div class="service-photo" role="img" aria-label="Photograph of block paving and brickwork" style="background:linear-gradient(135deg,#c9b3a0,#9a7d68)"></div>
    <div class="service-name">Paving &amp; Brickwork</div>
    <p class="service-text">Patios, paths and brick walls finished in natural stone, slate and clay.</p>
  </div>
  <div class="abs service" style="left:760px">
    <div class="service-photo" role="img" aria-label="Photograph of new timber fence panels" style="background:linear-gradient(135deg,#a98358,#6e5232)"></div>
    <div class="service-name">Fencing &amp; Decking</div>
    <p class="service-text">Close board, panel and picket fencing with decks built to stand firm.</p>
  </div>
  <svg class="abs arrow" style="left:70px" width="30" height="60" viewBox="0 0 30 60"><path d="M26 4 L4 30 L26 56" fill="none" stroke="#8a8a8a" stroke-width="3"/></svg>
  <svg class="abs arrow" style="left:1100px" width="30" height="60" viewBox="0 0 30 60"><path d="M4 4 L26 30 L4 56" fill="none" stroke="#8a8a8a" stroke-width="3"/></svg>

  <svg class="abs" style="left:0;top:2080px" width="1200" height="200" viewBox="0 2080 1200 200">
    <path d="M0 2236 C 420 2250, 880 2200, 1200 2090 L1200 2280 L0 2280 Z" fill="#ffffff"/>
    <path d="M0 2226 C 420 2240, 880 2190, 1200 2080" fill="none" stroke="#6abf2e" stroke-width="7"/>
  </svg>

  <!-- gallery -->
  <h2 class="abs heading gallery-title">Our <span class="accent">Gallery</span></h2>
  <p class="abs gallery-intro">A few of the driveways, patios and fences we have finished for homes across Surrey. Every project is built to the same high standard.</p>

  <div class="abs tile" style="left:155px;top:2520px;width:295px;height:200px;background:linear-gradient(180deg,#7b6f58 0%,#6c8246 45%,#4f7530 100%)" role="img" aria-label="Photograph of a new lawn laid beside a timber fence"></div>
  <div class="abs tile" style="left:155px;top:2730px;width:295px;height:270px;background:linear-gradient(180deg,#c99d6c,#9e7446)" role="img" aria-label="Photograph of freshly installed close board fencing"></div>
  <div class="abs tile" style="left:460px;top:2490px;width:300px;height:250px;background:linear-gradient(160deg,#d0cfcb,#8f8e8a)" role="img" aria-label="Photograph of grey stone steps and paving"></div>
  <div class="abs tile" style="left:460px;top:2750px;width:300px;height:250px;background:linear-gradient(180deg,#8a8e93 0%,#6c8e3e 50%,#476b25 100%)" role="img" aria-label="Photograph of a lawn edged by a raised brick wall"></div>
  <div class="abs tile" style="left:770px;top:2520px;width:305px;height:150px;background:linear-gradient(180deg,#5e4a36 0%,#6da03a 45%,#4e8526 100%)" role="img" aria-label="Photograph of a garden lawn with a fence behind"></div>
  <div class="abs tile" style="left:770px;top:2680px;width:305px;height:320px;background:linear-gradient(150deg,#b8b1a6,#9c7e6a 60%,#a9a49c)" role="img" aria-label="Photograph of a patio in sandstone slabs with brick border"></div>

  <!-- testimonials -->
  <div class="abs reviews-bg"></div>
  <svg class="abs" style="left:0;top:3020px" width="1200" height="160" viewBox="0 3020 1200 160">
    <path d="M0 3020 L1200 3020 L1200 3130 C 820 3060, 380 3050, 0 3100 Z" fill="#ffffff"/>
    <path d="M0 3110 C 380 3060, 820 3070, 1200 3140" fill="none" stroke="#6abf2e" stroke-width="7"/>
  </svg>
  <h2 class="abs heading reviews-title">What our <span class="accent">Customers</span> say</h2>
  <p class="abs reviews-quote">The team laid our new patio and side path in under a week and the finish is superb. They explained every step, kept the garden clean each evening and the price never changed from the quote. Our neighbours have already asked for their number and we will be using them again for the front driveway next spring.</p>
  <div class="abs reviews-name">Customer in Horley</div>
  <div class="abs reviews-dots"><span class="on"></span><span></span><span></span><span></span><span></span></div>

  <!-- footer -->
  <div class="abs footer"></div>
  <svg class="abs" style="left:0;top:3580px" width="1200" height="120" viewBox="0 3580 1200 120">
    <path d="M0 3580 L1200 3580 L1200 3600 C 800 3690, 400 3690, 0 3620 Z" fill="#e8e8e8"/>
    <path d="M0 3614 C 400 3684, 800 3684, 1200 3594" fill="none" stroke="#6abf2e" stroke-width="6"/>
  </svg>

  <div class="abs footer-brand">Brackwell<br>Landscapes</div>
  <div class="abs social"><span></span><span></span><span></span><span></span></div>

  <div class="abs contact" style="top:3840px">
    <svg width="36" height="36" viewBox="0 0 36 36"><circle cx="18" cy="18" r="16" fill="none" stroke="#fff" stroke-width="1.5"/><path d="M18 9a6 6 0 0 0-6 6c0 4.5 6 12 6 12s6-7.5 6-12a6 6 0 0 0-6-6z" fill="#fff"/><circle cx="18" cy="15" r="2.2" fill="#0b0b0b"/></svg>
    <div>14 Quarry Lane, Unit 3<br>Reigate RH2 7QX</div>
  </div>
  <div class="abs contact" style="top:3910px">
    <svg width="36" height="36" viewBox="0 0 36 36"><circle cx="18" cy="18" r="16" fill="none" stroke="#fff" stroke-width="1.5"/><rect x="10" y="12" width="16" height="12" fill="none" stroke="#fff" stroke-width="1.5"/><path d="M10 12 L18 19 L26 12" fill="none" stroke="#fff" stroke-width="1.5"/></svg>
    <div>Email us<br>hello@brackwell-example.co.uk</div>
  </div>
  <div class="abs contact" style="top:3980px">
    <svg width="36" height="36" viewBox="0 0 36 36"><circle cx="18" cy="18" r="16" fill="none" stroke="#fff" stroke-width="1.5"/><path d="M13.5 15.5a10 10 0 0 0 7 7l1.8-1.8c.3-.3.6-.3.9-.2.8.3 1.7.4 2.5.4.4 0 .7.3.7.7V25c0 .4-.3.7-.7.7A13 13 0 0 1 10.3 12.7c0-.4.3-.7.7-.7h2.4c.4 0 .7.3.7.7 0 .9.1 1.7.4 2.5.1.3 0 .6-.2.9z" fill="#fff"/></svg>
    <div>Phone<br>01632 960 972</div>
  </div>

  <div class="abs form">
    <div class="form-label">Name</div>
    <div class="field">Name</div>
    <div class="field">Phone</div>
    <div class="field">Email</div>
    <div class="field tall">Message</div>
    <div class="btn submit">Submit</div>
  </div>

  <div class="abs copyright">Copyright 2020 All Rights Reserved</div>
</div>
</body>
</html>
```